Business Card Design Project

We need a Business Card for an Mechanical Engineering firm in Singapore. The design should be Modern & Technical looking, yet eye catching.

Our company deals in Cutting Tools & Machine Accessories for the Manufacturing Industries such as Oil & Gas, Aero Space, etc... For more information on our Company, you can either email me or view our website www.valtrion.com.sg.

We are trying to revamp our image to give our consumers a fresh new perspective to our company, so we welcome all ideas.

Industry/Entity Type

Business

Requirements
Must have
• Must incorporate New Company Logo into the card as shown in Uploaded file.

```html
<!DOCTYPE html>
<html lang="en">
<head>
<meta charset="UTF-8">
<title>Valtrion Tools — Business Card</title>
<link href="https://fonts.googleapis.com/css2?family=Bebas+Neue&family=Oswald:wght@400;500&display=swap" rel="stylesheet">
<style>
  :root {
    --brand-red: #930034;
    --paper: #ffffff;
    --ink: #2a2a2a;
    --pattern-light: #f1f1f1;
    --pattern-mid: #dedede;
    --stage: #ffffff;
  }
  * { margin: 0; padding: 0; box-sizing: border-box; }
  html, body {
    width: 1200px; height: 900px; overflow: hidden;
    background: var(--stage);
  }
  .canvas { position: relative; width: 1200px; height: 900px; }
  .card {
    position: absolute; top: 306px; width: 504px; height: 288px;
    background: var(--paper); overflow: hidden;
    box-shadow: 0 1px 4px rgba(0,0,0,0.18);
  }
  .card--front { left: 58px; }
  .card--back { left: 638px; }

  .front__band-top {
    position: absolute; left: 0; top: 0; width: 100%; height: 150px;
    background: var(--brand-red);
  }
  .front__rule {
    position: absolute; left: 32px; top: 132px; width: 450px; height: 3px;
    background: var(--paper);
  }
  .front__band-bottom {
    position: absolute; left: 0; bottom: 0; width: 100%; height: 26px;
    background: var(--brand-red);
  }
  .front__heading {
    position: absolute; left: 32px; top: 40px;
    display: flex; align-items: flex-end; gap: 6px;
  }
  .front__number {
    font-family: 'Bebas Neue', sans-serif; font-size: 96px; line-height: 0.86;
    color: var(--paper); letter-spacing: 0;
    flex: none;
  }
  .front__address {
    font-family: 'Oswald', sans-serif; font-size: 8px; line-height: 10px;
    font-weight: 500; color: var(--paper); text-transform: uppercase;
    padding-bottom: 1px; white-space: nowrap;
  }
  .contact {
    position: absolute; left: 348px; top: 164px;
    font-family: 'Oswald', sans-serif; color: var(--brand-red);
  }
  .contact__name {
    font-family: 'Bebas Neue', sans-serif; font-size: 32px; line-height: 1;
    font-weight: 400; letter-spacing: 0.5px;
  }
  .contact__role {
    font-size: 8px; line-height: 11px; text-transform: uppercase; font-weight: 500;
    letter-spacing: 0.5px;
  }
  .contact__line { font-size: 9px; line-height: 11px; font-weight: 400; color: var(--brand-red); }

  .back__pattern {
    position: absolute; inset: 0;
    background: radial-gradient(circle at 50% 50%, var(--pattern-light), var(--pattern-mid));
  }
  .back__brand {
    position: absolute; left: 0; top: 0; width: 100%; height: 100%;
    display: flex; align-items: center; justify-content: center; gap: 12px;
  }
  .back__mark {
    width: 34px; height: 34px; border-radius: 50%; background: var(--brand-red);
  }
  .back__name {
    font-family: 'Bebas Neue', sans-serif; font-size: 44px; line-height: 1;
    color: var(--ink); letter-spacing: 1px;
  }
</style>
</head>
<body>
<main class="canvas">
  <section class="card card--front" aria-label="Business card front">
    <div class="front__band-top"></div>
    <div class="front__heading">
      <div class="front__number">218</div>
      <p class="front__address">Kallang Way #03-12,<br>Kallang Industrial Hub,<br>Singapore 349250</p>
    </div>
    <div class="front__rule"></div>
    <div class="contact">
      <h1 class="contact__name">MEREDITH</h1>
      <p class="contact__role">Sales Manager</p>
      <p class="contact__line">+65-63918204</p>
      <p class="contact__line">+65-63918205</p>
      <p class="contact__line">sales&#64;valtrion&#46;com&#46;sg</p>
    </div>
    <div class="front__band-bottom"></div>
  </section>

  <section class="card card--back" aria-label="Business card back">
    <div class="back__pattern" role="img" aria-label="Light grey background pattern of outlined gear shapes"></div>
    <div class="back__brand">
      <span class="back__mark"></span>
      <span class="back__name">VALTRION TOOLS</span>
    </div>
  </section>
</main>
</body>
</html>
```